Update cover page from corporate ppt template

We would like you to design a new cover page for our corporate presentation template

Attached you will find our existing template with the previous cover pages used in the past years.

As you can see, we have used transparency lines in different directions and also tried to develop a new design with mosaic/squares but we are not entirely satisfied (logo lost in the sky, ...)

You can reuse the same picture (mountain with the bridge, i.e not the one of the last cover page)

Feel free to come up with new ideas

```html
<!DOCTYPE html>
<html lang="en">
<head>
<meta charset="utf-8">
<title>Board of Directors – Cover and Closing Slides</title>
<link rel="stylesheet" href="https://fonts.googleapis.com/css2?family=Poppins:wght@400;500;600;700;800&display=swap">
<style>
  :root {
    --canvas: #ffffff;
    --brand-blue: #7089c8;
    --brand-blue-soft: #8ba0d0;
    --brand-blue-pale: #c7d1ea;
    --accent-line: #6f8fd6;
    --ink-white: #ffffff;
    --ink-grey: #7a7a7a;
    --brand-grey: #6e6e6e;
  }
  * { box-sizing: border-box; margin: 0; padding: 0; }
  html, body { width: 1064px; height: 1200px; overflow: hidden; background: var(--canvas); }
  body { position: relative; font-family: "Poppins", sans-serif; }

  .slide { position: absolute; width: 505px; height: 378px; overflow: hidden; }
  .slide > svg { position: absolute; inset: 0; width: 100%; height: 100%; display: block; }
  .slide--forest-cover  { left: 20px;  top: 18px; }
  .slide--forest-close  { left: 538px; top: 18px; }
  .slide--diagonal-cover { left: 20px;  top: 410px; }
  .slide--diagonal-close { left: 539px; top: 411px; }
  .slide--lake-cover    { left: 20px;  top: 804px; }
  .slide--lake-close    { left: 539px; top: 804px; }

  .cover-title { position: absolute; color: var(--ink-white); font-weight: 800; line-height: 1.12; white-space: nowrap; }
  .closing-title { position: absolute; color: var(--ink-white); font-weight: 700; white-space: nowrap; line-height: 1; }
  .title-rule { position: absolute; width: 43px; height: 3px; background: var(--accent-line); }
  .title-rule--light { background: rgba(255,255,255,.8); }
  .cover-date { position: absolute; color: var(--ink-white); font-size: 13px; font-weight: 400; line-height: 1; }

  .brand-name { position: absolute; transform: translate(-50%, -50%); font-weight: 500;
                color: var(--brand-grey); letter-spacing: .04em; white-space: nowrap; line-height: 1; }

  .centered { position: absolute; left: 0; right: 0; text-align: center; line-height: 1; white-space: nowrap; }
  .lake-title { font-size: 30px; font-weight: 700; color: var(--ink-grey); }
  .lake-date { font-size: 10px; font-weight: 400; color: var(--ink-grey); }
  .lake-closing { font-size: 30px; font-weight: 800; color: var(--ink-white); }
</style>
</head>
<body>

<section class="slide slide--forest-cover" aria-label="Cover slide, forest and lake">
  <svg viewBox="0 0 505 378" preserveAspectRatio="none">
    <defs>
      <linearGradient id="forestCover" x1="0" y1="0" x2="1" y2="0">
        <stop offset="0" stop-color="#3a5520"/><stop offset=".35" stop-color="#5b7428"/>
        <stop offset=".55" stop-color="#6d7f33"/><stop offset=".62" stop-color="#8fd2c4"/>
        <stop offset="1" stop-color="#d6eee9"/>
      </linearGradient>
    </defs>
    <rect role="img" aria-label="Aerial photo of a winding road between pine forest and a turquoise lake" width="505" height="378" fill="url(#forestCover)"/>
    <ellipse cx="410" cy="265" rx="140" ry="150" fill="#ffffff" opacity=".6"/>
  </svg>
  <div class="cover-title" style="left:48px;top:42px;font-size:36px;">Board of<br>Directors</div>
  <div class="title-rule" style="left:48px;top:148px;"></div>
  <div class="cover-date" style="left:48px;top:172px;">May 2024</div>
  <div class="brand-name" style="left:384px;top:240px;font-size:32px;">Veranta</div>
</section>

<section class="slide slide--forest-close" aria-label="Closing slide, forest and lake">
  <svg viewBox="0 0 505 378" preserveAspectRatio="none">
    <defs>
      <linearGradient id="forestClose" x1="1" y1="0" x2="0" y2="0">
        <stop offset="0" stop-color="#3a5520"/><stop offset=".35" stop-color="#5b7428"/>
        <stop offset=".55" stop-color="#6d7f33"/><stop offset=".62" stop-color="#8fd2c4"/>
        <stop offset="1" stop-color="#d6eee9"/>
      </linearGradient>
    </defs>
    <rect role="img" aria-label="Mirrored aerial photo of a winding road between pine forest and a turquoise lake" width="505" height="378" fill="url(#forestClose)"/>
    <ellipse cx="95" cy="265" rx="140" ry="150" fill="#ffffff" opacity=".6"/>
  </svg>
  <div class="closing-title" style="left:318px;top:68px;font-size:27px;">Thank You</div>
  <div class="brand-name" style="left:122px;top:244px;font-size:32px;">Veranta</div>
</section>

<section class="slide slide--diagonal-cover" aria-label="Cover slide, diagonal bands">
  <svg viewBox="0 0 505 378" preserveAspectRatio="none">
    <defs>
      <linearGradient id="alpsCover" x1="0" y1="0" x2="0" y2="1">
        <stop offset="0" stop-color="#5b9ce0"/><stop offset=".3" stop-color="#9aa7b6"/>
        <stop offset=".5" stop-color="#56604c"/><stop offset=".75" stop-color="#4e6a22"/>
        <stop offset="1" stop-color="#a49a2c"/>
      </linearGradient>
    </defs>
    <rect width="505" height="378" fill="#ffffff"/>
    <polygon role="img" aria-label="Photo of alpine mountains with a suspension bridge over a forested valley" points="344,0 505,0 505,150 292,378 56,378" fill="url(#alpsCover)"/>
    <polygon points="0,0 344,0 56,378 0,378" fill="var(--brand-blue)"/>
    <polygon points="0,218 110,290 60,378 0,378" fill="#8ea4d6" opacity=".7"/>
    <polygon points="344,0 372,0 86,378 58,378" fill="#ffffff" opacity=".5"/>
    <polygon points="392,0 416,0 130,378 106,378" fill="#ffffff" opacity=".35"/>
    <polygon points="505,40 505,98 300,378 250,378" fill="#ffffff" opacity=".45"/>
    <polygon points="470,150 505,170 505,250 440,200" fill="var(--brand-blue-pale)" opacity=".8"/>
  </svg>
  <div class="cover-title" style="left:48px;top:58px;font-size:31px;font-weight:700;">Board of<br>Directors</div>
  <div class="title-rule title-rule--light" style="left:48px;top:148px;"></div>
  <div class="cover-date" style="left:48px;top:178px;">May 2024</div>
  <div class="brand-name" style="left:428px;top:320px;font-size:24px;">Veranta</div>
</section>

<section class="slide slide--diagonal-close" aria-label="Closing slide, diagonal bands">
  <svg viewBox="0 0 505 378" preserveAspectRatio="none">
    <defs>
      <linearGradient id="alpsClose" x1="0" y1="0" x2="0" y2="1">
        <stop offset="0" stop-color="#4f95dc"/><stop offset=".28" stop-color="#9bc3e8"/>
        <stop offset=".42" stop-color="#6d7686"/><stop offset=".65" stop-color="#556826"/>
        <stop offset="1" stop-color="#7a8d2e"/>
      </linearGradient>
    </defs>
    <rect width="505" height="378" fill="#ffffff"/>
    <polygon role="img" aria-label="Photo of snowy alpine peaks and a forested valley with a suspension bridge" points="0,0 395,0 115,378 0,378" fill="url(#alpsClose)"/>
    <polygon points="395,0 425,0 145,378 115,378" fill="#c9dcf2" opacity=".6"/>
    <polygon points="440,0 460,0 180,378 160,378" fill="#c9dcf2" opacity=".45"/>
  </svg>
  <div class="closing-title" style="left:41px;top:50px;font-size:27px;">Thank You</div>
  <div class="brand-name" style="left:374px;top:301px;font-size:34px;">Veranta</div>
</section>

<section class="slide slide--lake-cover" aria-label="Cover slide, mountain lake">
  <svg viewBox="0 0 505 378" preserveAspectRatio="none">
    <defs>
      <linearGradient id="lakeCover" x1="0" y1="0" x2="0" y2="1">
        <stop offset="0" stop-color="#2f8ddf"/><stop offset=".28" stop-color="#a9d3f3"/>
        <stop offset=".45" stop-color="#8e95a4"/><stop offset=".58" stop-color="#9a7a30"/>
        <stop offset=".72" stop-color="#2f3a2c"/><stop offset="1" stop-color="#9aa06a"/>
      </linearGradient>
    </defs>
    <rect role="img" aria-label="Photo of snowy mountain peaks reflected in an alpine lake under a clear sky" width="505" height="378" fill="url(#lakeCover)"/>
    <path d="M0,100 Q250,125 505,95 L505,110 Q250,140 0,115 Z" fill="#ffffff" opacity=".35"/>
    <path d="M0,262 Q250,235 505,262 L505,378 L0,378 Z" fill="var(--brand-blue-pale)" opacity=".9"/>
    <path d="M0,272 Q250,245 505,272 L505,378 L0,378 Z" fill="#f5f6f7" opacity=".95"/>
  </svg>
  <div class="brand-name" style="left:252px;top:66px;font-size:34px;">Veranta</div>
  <div class="centered lake-title" style="top:291px;">Board of Directors</div>
  <div class="centered lake-date" style="top:327px;">May 2024</div>
</section>

<section class="slide slide--lake-close" aria-label="Closing slide, mountain lake">
  <svg viewBox="0 0 505 378" preserveAspectRatio="none">
    <defs>
      <linearGradient id="lakeClose" x1="0" y1="0" x2="0" y2="1">
        <stop offset="0" stop-color="#2f8ddf"/><stop offset=".28" stop-color="#a9d3f3"/>
        <stop offset=".45" stop-color="#8e95a4"/><stop offset=".58" stop-color="#9a7a30"/>
        <stop offset=".72" stop-color="#2f3a2c"/><stop offset="1" stop-color="#9aa06a"/>
      </linearGradient>
    </defs>
    <rect role="img" aria-label="Photo of snowy mountain peaks reflected in an alpine lake under a clear sky" width="505" height="378" fill="url(#lakeClose)"/>
    <path d="M0,100 Q250,125 505,95 L505,110 Q250,140 0,115 Z" fill="#ffffff" opacity=".35"/>
    <path d="M0,262 Q250,240 505,262 L505,378 L0,378 Z" fill="var(--brand-blue-pale)"/>
    <path d="M0,272 Q250,250 505,278 L505,378 L0,378 Z" fill="var(--brand-blue-soft)"/>
  </svg>
  <div class="brand-name" style="left:252px;top:66px;font-size:34px;">Veranta</div>
  <div class="centered lake-closing" style="top:305px;">Thank You</div>
</section>

</body>
</html>
```